Webpage for balustrade importer and installer

We are a balustrade importer and installer. We sell a few different products mostly connected with glass and aluminum. We sell balconies, stairs, shower glass, mirrors, splash back glass, office partitions, glass dors and walls.

Coded - Design and coding required

```html
<!DOCTYPE html>
<html lang="en">
<head>
<meta charset="utf-8">
<title>GLERVIK — Glass &amp; Aluminium Balustrades</title>
<link rel="stylesheet" href="https://fonts.googleapis.com/css2?family=Roboto:wght@300;400;500;700&family=Lato:wght@300;400;700&display=swap">
<style>
:root{
  --blue:#3a5ba8;
  --blue-dark:#2f4c91;
  --ink:#1d1f24;
  --muted:#8c8f96;
  --band:#f2f4f9;
  --footer:#1c1f2d;
  --white:#ffffff;
}
*{box-sizing:border-box;margin:0;padding:0}
html,body{width:1200px;height:4311px;overflow:hidden}
body{position:relative;background:var(--white);font-family:"Lato",sans-serif;color:var(--ink)}
.abs{position:absolute}
.center{text-align:center}
.brand{font-family:"Roboto",sans-serif;font-weight:300;color:var(--blue);letter-spacing:1px}
.nav{position:absolute;top:56px;right:92px;display:flex;gap:36px;font-family:"Lato",sans-serif;font-size:12px;color:#333}
.nav a{color:inherit;text-decoration:none}
.nav .active{font-weight:700}
.contact-top{position:absolute;top:8px;left:968px;display:flex;gap:10px;align-items:center}
.contact-top .icon{width:22px;height:22px;border:1px solid #cfd4e0;display:flex;align-items:center;justify-content:center}
.contact-top strong{display:block;font-family:"Roboto",sans-serif;font-size:14px;font-weight:500;color:var(--ink)}
.contact-top span{font-size:11px;color:var(--muted)}
.photo{position:absolute}
.btn{position:absolute;display:flex;align-items:center;justify-content:center;gap:7px;background:var(--blue);color:var(--white);font-family:"Lato",sans-serif;font-weight:700;font-size:11px;letter-spacing:.3px;height:35px;width:112px}
.btn i{width:12px;height:12px;border-radius:50%;background:var(--white);display:inline-block;position:relative}
.btn i::after{content:"";position:absolute;left:3px;top:3px;border-left:5px solid var(--blue);border-top:3px solid transparent;border-bottom:3px solid transparent}
.section-title{position:absolute;left:0;width:1200px;text-align:center;font-family:"Roboto",sans-serif;font-weight:700;font-size:36px;color:var(--ink);text-transform:uppercase}
.section-title em{font-style:normal;color:var(--blue)}
.body-text{font-size:13px;line-height:21px;color:var(--muted);font-weight:300}
.hero-text{position:absolute;left:94px;color:var(--white)}
.card-title,.row-title{font-family:"Roboto",sans-serif;font-size:21px;font-weight:400;color:var(--ink);text-transform:uppercase}
.blog-title{font-family:"Roboto",sans-serif;font-weight:500;font-size:17px;line-height:21px;color:var(--ink)}
footer{position:absolute;left:0;top:4004px;width:1200px;height:307px;background:var(--footer);color:#c8cbd4}
footer h4{position:absolute;top:46px;font-family:"Roboto",sans-serif;font-weight:400;font-size:17px;color:var(--white);letter-spacing:.5px}
footer ul{position:absolute;top:80px;list-style:none;font-size:11px;line-height:27px}
.field{position:absolute;left:887px;width:220px;height:30px;background:var(--white);font-size:10px;color:#555;padding:9px 8px}
.social{position:absolute;top:4200px;width:26px;height:26px;border-radius:50%}
</style>
</head>
<body>

<header>
  <div class="abs brand" style="left:94px;top:14px;font-size:36px;line-height:44px">GLERVIK</div>
  <div class="contact-top">
    <div class="icon"><svg width="12" height="12" viewBox="0 0 12 12"><path d="M1 6 L11 1 L8 11 L6 7 Z" fill="none" stroke="#3a5ba8" stroke-width="1.2"/></svg></div>
    <div><strong>+2 (555) 240 7300</strong><span>hello@glervik.example</span></div>
  </div>
  <nav class="nav"><a class="active">HOME</a><a>ABOUT US</a><a>PRODUCTS</a><a>BLOG</a><a>CONTACT US</a></nav>
  <div class="abs" style="left:0;top:73px;width:1200px;height:1px;background:#e6e8ee"></div>
</header>

<section class="hero">
  <div class="photo" role="img" aria-label="Modern glass villa with reflecting pool at sunset" style="left:0;top:74px;width:1200px;height:525px;background:linear-gradient(180deg,#4b5a6d 0%,#8d8a7e 30%,#c9a464 42%,#3d4f66 58%,#20486e 80%,#2a5b85 100%)"></div>
  <div class="hero-text" style="top:282px;font-family:'Lato',sans-serif;font-weight:300;font-size:29px">FINIBUS</div>
  <div class="hero-text" style="top:314px;font-family:'Roboto',sans-serif;font-weight:700;font-size:45px;line-height:50px">Bonorum Lorem</div>
  <div class="hero-text" style="top:364px;font-family:'Roboto',sans-serif;font-weight:400;font-size:35px">Malorum</div>
  <div class="hero-text" style="top:408px;font-size:13px;line-height:18px;width:310px">Sed ut perspiciatis unde omnis iste natus error sit voluptatem</div>
  <div class="btn" style="left:94px;top:465px">READ MORE <i></i></div>
  <div class="abs" style="left:588px;top:593px;display:flex;gap:4px">
    <span style="width:6px;height:6px;border-radius:50%;background:#3a5ba8"></span>
    <span style="width:6px;height:6px;border-radius:50%;background:#3a5ba8"></span>
    <span style="width:6px;height:6px;border-radius:50%;background:#3a5ba8"></span>
  </div>
</section>

<section class="intro">
  <div class="photo" role="img" aria-label="Bright interior staircase with glass balustrade and plant" style="left:94px;top:653px;width:499px;height:289px;background:linear-gradient(160deg,#e8e6e2,#cfc9bf 55%,#b68a5c)"></div>
  <div class="photo" role="img" aria-label="Curved glass balustrade with steel handrail" style="left:606px;top:653px;width:501px;height:289px;background:linear-gradient(135deg,#a9afb4,#d6dade 45%,#6f7880)"></div>
  <div class="abs center" style="left:0;width:1200px;top:1000px;font-size:18px;font-weight:300;color:#444">WELCOME TO</div>
  <div class="abs center brand" style="left:0;width:1200px;top:1022px;font-size:36px;font-weight:500">GLERVIK</div>
  <p class="abs center body-text" style="left:94px;width:1013px;top:1080px">Sed ut perspiciatis unde omnis iste natus error sit voluptatem accusantium doloremque laudantium, totam rem aperiam, eaque ipsa quae ab illo inventore veritatis et quasi architecto beatae vitae dicta sunt explicabo. Nemo enim ipsam voluptatem quia voluptas sit aspernatur aut odit aut fugit, sed quia consequuntur magni dolores eos qui ratione voluptatem sequi nesciunt. Neque porro quisquam est, qui dolorem ipsum quia dolor sit amet, consectetur, adipisci velit, sed quia non numquam eius modi tempora incidunt ut labore et dolore magnam aliquam quaerat voluptatem.</p>
  <div class="btn" style="left:544px;top:1187px">READ MORE <i></i></div>
</section>

<section class="featured">
  <h2 class="section-title" style="top:1270px"><em>Featured</em> Products</h2>

  <div class="photo" role="img" aria-label="Balcony with glass railing overlooking landscape" style="left:94px;top:1348px;width:330px;height:323px;background:linear-gradient(180deg,#9aa7b6,#7c7a74 50%,#55575a);clip-path:polygon(0 0,100% 0,100% 100%,0 100%)"></div>
  <div class="photo" role="img" aria-label="Floating staircase with glass balustrade" style="left:435px;top:1348px;width:330px;height:323px;background:linear-gradient(180deg,#cfd2d4,#8c9196 55%,#5f6469)"></div>
  <div class="photo" role="img" aria-label="Bathroom with frameless glass shower" style="left:777px;top:1348px;width:330px;height:323px;background:linear-gradient(90deg,#c7c9cd,#2f3c69 45%,#3a4676 75%,#c7a57c)"></div>
  <svg class="abs" style="left:0;top:1620px" width="1200" height="60" viewBox="0 0 1200 60">
    <polygon points="94,60 424,51 424,60" fill="#fff"/>
    <polygon points="94,60 244,20 424,52 424,60" fill="#fff"/>
    <polygon points="435,60 585,20 765,52 765,60" fill="#fff"/>
    <polygon points="777,60 927,20 1107,52 1107,60" fill="#fff"/>
  </svg>

  <div class="abs center card-title" style="left:94px;width:330px;top:1676px">Balconies</div>
  <div class="abs center card-title" style="left:435px;width:330px;top:1676px">Stairs</div>
  <div class="abs center card-title" style="left:777px;width:330px;top:1676px">Shower Glass</div>
  <p class="abs center body-text" style="left:104px;width:310px;top:1712px">Sed ut perspiciatis unde omnis iste natus error sit voluptatem accusantium</p>
  <p class="abs center body-text" style="left:445px;width:310px;top:1712px">Sed ut perspiciatis unde omnis iste natus error sit voluptatem accusantium</p>
  <p class="abs center body-text" style="left:787px;width:310px;top:1712px">Sed ut perspiciatis unde omnis iste natus error sit voluptatem accusantium</p>
  <div class="btn" style="left:203px;top:1765px">VIEW DETAILS <i></i></div>
  <div class="btn" style="left:544px;top:1765px">VIEW DETAILS <i></i></div>
  <div class="btn" style="left:886px;top:1765px">VIEW DETAILS <i></i></div>
</section>

<section class="review">
  <svg class="abs" style="left:0;top:1810px" width="1200" height="520" viewBox="0 0 1200 520">
    <polygon points="0,250 1200,3 1200,266 0,508" fill="#f2f4f9"/>
  </svg>
  <h2 class="section-title" style="top:1860px"><em>Customer</em> Review</h2>
  <div class="abs" role="img" aria-label="Customer portrait" style="left:556px;top:1936px;width:88px;height:88px;border-radius:50%;background:radial-gradient(circle,#b89a84,#e2e4e8 70%)"></div>
  <div class="abs center" style="left:0;width:1200px;top:2036px;font-family:'Roboto',sans-serif;font-size:17px;color:var(--ink)">Mr. Jhon Doe</div>
  <div class="abs center" style="left:0;width:1200px;top:2058px;font-size:9px;color:#666">ARCHITECHTURE</div>
  <p class="abs center body-text" style="left:150px;width:900px;top:2086px">Sed ut perspiciatis unde omnis iste natus error sit voluptatem accusantium doloremque laudantium, totam rem aperiam, eaque ipsa quae ab illo inventore veritatis et quasi architecto beatae vitae dicta sunt explicabo. Nemo enim ipsam voluptatem quia voluptas sit aspernatur aut odit aut fugit, sed quia consequuntur magni dolores eos qui ratione voluptatem sequi nesciunt.</p>
  <div class="abs" style="left:570px;top:2170px;display:flex;gap:4px">
    <span style="width:18px;height:2px;background:var(--blue)"></span>
    <span style="width:18px;height:2px;background:var(--ink)"></span>
    <span style="width:18px;height:2px;background:var(--ink)"></span>
  </div>
</section>

<section class="best-selling">
  <h2 class="section-title" style="top:2221px"><em>Best</em> Selling</h2>

  <div class="photo" role="img" aria-label="White bathroom with vanity mirrors" style="left:94px;top:2302px;width:505px;height:306px;background:linear-gradient(135deg,#ececeb,#c9c9c7 50%,#8e8f90)"></div>
  <div class="abs center row-title" style="left:603px;width:505px;top:2376px">Mirrors</div>
  <p class="abs center body-text" style="left:633px;width:445px;top:2414px">Sed ut perspiciatis unde omnis iste natus error sit voluptatem accusantium doloremque laudantium, totam rem aperiam, eaque ipsa quae ab illo inventore veritatis et quasi architecto beatae vitae dicta sunt explicabo.</p>
  <div class="btn" style="left:798px;top:2496px">VIEW DETAILS <i></i></div>

  <div class="photo" role="img" aria-label="Dark kitchen with glass splash back" style="left:603px;top:2610px;width:505px;height:306px;background:linear-gradient(160deg,#c8c3bb,#4a4440 50%,#2f2a27 75%,#8b6b4c)"></div>
  <div class="abs center row-title" style="left:94px;width:505px;top:2684px">Splash Back Glass</div>
  <p class="abs center body-text" style="left:124px;width:445px;top:2722px">Sed ut perspiciatis unde omnis iste natus error sit voluptatem accusantium doloremque laudantium, totam rem aperiam, eaque ipsa quae ab illo inventore veritatis et quasi architecto beatae vitae dicta sunt explicabo.</p>
  <div class="btn" style="left:271px;top:2804px">VIEW DETAILS <i></i></div>

  <div class="photo" role="img" aria-label="Open office with glass partitions and desks" style="left:94px;top:2918px;width:505px;height:306px;background:linear-gradient(180deg,#e9ecef,#c5cbd1 55%,#3b3e45)"></div>
  <div class="abs center row-title" style="left:603px;width:505px;top:2992px">Office Partitions</div>
  <p class="abs center body-text" style="left:633px;width:445px;top:3030px">Sed ut perspiciatis unde omnis iste natus error sit voluptatem accusantium doloremque laudantium, totam rem aperiam, eaque ipsa quae ab illo inventore veritatis et quasi architecto beatae vitae dicta sunt explicabo.</p>
  <div class="btn" style="left:798px;top:3112px">VIEW DETAILS <i></i></div>

  <div class="photo" role="img" aria-label="Corridor lined with glass doors and walls" style="left:603px;top:3226px;width:505px;height:306px;background:linear-gradient(90deg,#2e2b28,#b9b3aa 50%,#2e2b28)"></div>
  <div class="abs center row-title" style="left:94px;width:505px;top:3300px">Glass Doors and Walls</div>
  <p class="abs center body-text" style="left:124px;width:445px;top:3338px">Sed ut perspiciatis unde omnis iste natus error sit voluptatem accusantium doloremque laudantium, totam rem aperiam, eaque ipsa quae ab illo inventore veritatis et quasi architecto beatae vitae dicta sunt explicabo.</p>
  <div class="btn" style="left:271px;top:3420px">VIEW DETAILS <i></i></div>
</section>

<section class="blog">
  <h2 class="section-title" style="top:3594px"><em>Recent</em> Blog</h2>
  <div class="photo" role="img" aria-label="House with railed balcony" style="left:94px;top:3654px;width:329px;height:143px;background:linear-gradient(180deg,#b9c1cc,#6e6a63 60%,#3d3b38)"></div>
  <div class="photo" role="img" aria-label="Snowy terrace railing at dusk" style="left:436px;top:3654px;width:329px;height:143px;background:linear-gradient(180deg,#5d6f94,#8fa0c0 55%,#d8dde8)"></div>
  <div class="photo" role="img" aria-label="Balcony railing overlooking coast at dusk" style="left:778px;top:3654px;width:329px;height:143px;background:linear-gradient(180deg,#7b7f95,#b0a69c 50%,#3f3b3f)"></div>

  <div class="abs blog-title" style="left:94px;width:320px;top:3826px">Nemo enim ipsam voluptatem quia voluptas</div>
  <div class="abs blog-title" style="left:436px;width:320px;top:3826px">Nemo enim ipsam voluptatem quia voluptas</div>
  <div class="abs blog-title" style="left:778px;width:320px;top:3826px">Nemo enim ipsam voluptatem quia voluptas</div>
  <p class="abs body-text" style="left:94px;width:310px;top:3870px">Sed ut perspiciatis unde omnis iste natus error sit voluptatem accusantium doloremque...</p>
  <p class="abs body-text" style="left:436px;width:310px;top:3870px">Sed ut perspiciatis unde omnis iste natus error sit voluptatem accusantium doloremque...</p>
  <p class="abs body-text" style="left:778px;width:310px;top:3870px">Sed ut perspiciatis unde omnis iste natus error sit voluptatem accusantium doloremque...</p>
  <div class="btn" style="left:94px;top:3919px">READ MORE <i></i></div>
  <div class="btn" style="left:436px;top:3919px">READ MORE <i></i></div>
  <div class="btn" style="left:778px;top:3919px">READ MORE <i></i></div>
</section>

<footer>
  <div class="abs brand" style="left:94px;top:42px;font-size:38px;line-height:46px">GLERVIK</div>
  <div class="abs" style="left:94px;top:100px;font-size:11px;line-height:16px;display:flex;gap:6px">
    <svg width="9" height="12" viewBox="0 0 9 12"><path d="M4.5 12 C1 7 0 5.5 0 4.5 A4.5 4.5 0 0 1 9 4.5 C9 5.5 8 7 4.5 12Z" fill="#3a5ba8"/><circle cx="4.5" cy="4.5" r="1.6" fill="#1c1f2d"/></svg>
    <span>Harbour Lane 12, 220 Vesturbyr<br>Iceland</span>
  </div>
  <div class="abs" style="left:94px;top:144px;font-size:11px;display:flex;gap:6px;align-items:center">
    <svg width="10" height="10" viewBox="0 0 10 10"><path d="M2 0 L4 2.5 L3 4 C4 6 5 7 6.5 7.5 L8 6.5 L10 8.5 L8.5 10 C4 9.5 0.5 6 0 1.5Z" fill="#3a5ba8"/></svg>+2 (555) 240 7300
  </div>
  <div class="abs" style="left:94px;top:172px;font-size:11px;display:flex;gap:6px;align-items:center">
    <svg width="11" height="8" viewBox="0 0 11 8"><rect width="11" height="8" fill="#3a5ba8"/><path d="M0 0 L5.5 4.5 L11 0" fill="none" stroke="#1c1f2d"/></svg>hello@glervik.example
  </div>

  <h4 style="left:382px">SITEMAP</h4>
  <ul style="left:382px"><li>Home</li><li>About Us</li><li>Products</li><li>Blog</li><li>Contact Us</li></ul>
  <h4 style="left:619px">INFORMATION</h4>
  <ul style="left:619px"><li>Products Details</li><li>FAQ's</li><li>Privacy Policy</li><li>Terms &amp; Condition</li><li>Help</li></ul>
  <h4 style="left:887px">NEWSLETTER</h4>
  <div class="field" style="top:84px">Name:</div>
  <div class="field" style="top:117px">Email:</div>
  <div class="abs center" style="left:887px;top:154px;width:220px;height:28px;background:var(--blue);color:#fff;font-size:10px;font-weight:700;line-height:28px">SUBSCRIBE</div>
  <div class="abs center" style="left:0;width:1200px;top:250px;font-size:11px;color:#c8cbd4">COPYRIGHT © 2020 <span style="color:#5b7cd0">GLERVIK</span>. ALL RIGHTS RESERVED.</div>
</footer>
<div class="social" style="left:888px;background:#3a5ba8"></div>
<div class="social" style="left:918px;background:#1da1f2"></div>
<div class="social" style="left:948px;background:#f26522"></div>

</body>
</html>
```